どのご提案もとても素敵で大変迷いましたが、こちらの作品が一番イメージにあっておりましたので採用させて頂きました。
皆さま、この度は素敵なご提案をありがとうございました!初めての利用で至らない点も多々あったかと思いますが、ご親切に対応頂き感謝しております。また機会がありましたら依頼させて頂きますので、その時はどうぞよろしくお願い致します。
ネイルサロンのバナーデザイン バナー作成・バナーデザインの仕事の依頼
大変失礼いたしました。
こちらはバナー制作ではなく、ヘッダー画像の制作をお願いしたいと思っております。
度々、追記を失礼します。
希望サイズですが記載の正方形ではなく
横1367に合わせた長方形でお願いします。
現在のウェブサイトはこんな感じです。
https://vemosquaril.com/
ターゲット層は30代後半〜50代。
料金価格設定は少し高めのサロンです。
使用していただきたいコピー候補は、
「デザインも大事だけどとにかくキレイに塗ってほしい」
「爪周りや爪の形など指全体を美しくしたい」
「爪のダメージ最小限で長く健康的にネイルを楽しみたい」
ネイルメロウジュは「本物の高いクオリティのネイル」を求める大人女性のためのネイルサロンです。
★ネイリスト全員が検定1級・コンテスト受賞も多数
★カウンセリング・アフターフォローも徹底重視
★はじめての方も大歓迎
この辺を使っていただきたいと考えております。
写真の候補はこちらの三枚です。

```html
<!DOCTYPE html>
<html lang="ja">
<head>
<meta charset="utf-8">
<title>ネイルメロウジュ岡山 ヘッダー</title>
<link rel="stylesheet" href="https://fonts.googleapis.com/css2?family=Shippori+Mincho:wght@400;500;600;700&display=swap">
<style>
  :root {
    --ink: #4b4038;
    --ink-soft: #6a5d54;
    --gold: #b8913f;
    --gold-light: #d8bf85;
    --gold-wash: rgba(222, 196, 140, 0.35);
    --paper: #ffffff;
    --skin-1: #f3e3dc;
    --skin-2: #e9cfc4;
    --skin-3: #f7ece7;
  }
  * { margin: 0; padding: 0; box-sizing: border-box; }
  html, body { width: 1200px; height: 530px; overflow: hidden; background: var(--paper); }
  body { font-family: "Shippori Mincho", serif; color: var(--ink); }

  .header-banner { position: relative; width: 1200px; height: 530px; overflow: hidden; background: var(--paper); }

  .hands-photo {
    position: absolute; top: 0; right: 0; width: 760px; height: 530px;
    background:
      radial-gradient(ellipse 320px 200px at 62% 32%, var(--skin-2), transparent 70%),
      radial-gradient(ellipse 300px 220px at 70% 78%, var(--skin-1), transparent 72%),
      linear-gradient(180deg, var(--skin-3), var(--skin-1));
  }
  .photo-fade {
    position: absolute; top: 0; left: 0; width: 860px; height: 530px;
    background: linear-gradient(90deg, #fff 0%, #fff 55%, rgba(255,255,255,0.85) 72%, rgba(255,255,255,0) 100%);
  }

  .concerns { position: absolute; top: 26px; left: 56px; font-size: 19px; letter-spacing: 1px; color: var(--ink-soft); line-height: 1; }
  .concerns li { list-style: none; margin-bottom: 28px; }
  .concerns li:nth-child(2) { padding-left: 22px; }
  .concerns li:nth-child(3) { padding-left: 46px; }

  .salon-intro { position: absolute; top: 196px; left: 116px; font-size: 27px; font-weight: 500; color: var(--gold); letter-spacing: 2px; }

  .headline { position: absolute; top: 236px; left: 80px; font-size: 44px; font-weight: 500; letter-spacing: 1px; color: var(--ink); }
  .headline .quote { color: var(--ink); }

  .tagline { position: absolute; top: 294px; left: 218px; font-weight: 600; letter-spacing: 1px; color: var(--ink); }
  .tagline::after {
    content: ""; position: absolute; left: 0; right: 0; bottom: 4px; height: 16px;
    background: linear-gradient(90deg, transparent, var(--gold-wash) 10%, var(--gold-wash) 90%, transparent);
    z-index: -1;
  }
  .tagline .accent { color: var(--gold); font-size: 50px; font-weight: 700; }
  .tagline .small { font-size: 32px; }

  .features {
    position: absolute; top: 404px; left: 60px; width: 650px; height: 100px;
    border: 1.5px solid var(--gold-light); background: rgba(255,255,255,0.9);
    display: flex; align-items: center; padding-left: 20px; gap: 14px;
  }
  .seal { width: 86px; height: 86px; flex: none; position: relative; }
  .seal svg { position: absolute; inset: 0; }
  .seal-text { position: absolute; inset: 0; display: flex; flex-direction: column; align-items: center; justify-content: center; color: var(--gold); line-height: 1.15; text-align: center; }
  .seal-text .s { font-size: 12px; }
  .seal-text .l { font-size: 20px; font-weight: 700; }
  .feature-notes { margin-left: 20px; color: var(--ink); }
  .feature-notes .lead { font-size: 22px; font-weight: 600; letter-spacing: 1px; }
  .feature-notes .sub { font-size: 17px; margin-top: 6px; color: var(--ink-soft); }
</style>
</head>
<body>
  <div class="header-banner">
    <div class="hands-photo" role="img" aria-label="ナチュラルなグラデーションネイルを施した女性の手元の写真"></div>
    <div class="photo-fade"></div>

    <ul class="concerns">
      <li>『爪のダメージ最小限で長く健康的にネイルを楽しみたい』</li>
      <li>『デザインも大事だけどとにかくキレイに塗ってほしい』</li>
      <li>『爪周りや爪の形など指全体を美しくしたい』</li>
    </ul>

    <p class="salon-intro">ネイルメロウジュ岡山は</p>
    <h1 class="headline">「本物の高いクオリティのネイル」を求める</h1>
    <p class="tagline"><span class="accent">大人女性</span><span class="small">のための</span><span class="accent">ネイルサロン</span><span class="small">です</span></p>

    <div class="features">
      <div class="seal">
        <svg viewBox="0 0 86 86" width="86" height="86">
          <circle cx="43" cy="43" r="41" fill="none" stroke="#d8bf85" stroke-width="1.5" stroke-dasharray="3 2"/>
          <circle cx="43" cy="43" r="35" fill="none" stroke="#d8bf85" stroke-width="1"/>
        </svg>
        <div class="seal-text"><span class="s">ネイリスト全員が</span><span class="l">検定1級</span></div>
      </div>
      <div class="seal">
        <svg viewBox="0 0 86 86" width="86" height="86">
          <circle cx="43" cy="43" r="41" fill="none" stroke="#d8bf85" stroke-width="1.5" stroke-dasharray="3 2"/>
          <circle cx="43" cy="43" r="35" fill="none" stroke="#d8bf85" stroke-width="1"/>
        </svg>
        <div class="seal-text"><span class="s">コンテスト</span><span class="l">多数受賞</span></div>
      </div>
      <div class="feature-notes">
        <p class="lead">初めての方も大歓迎！</p>
        <p class="sub">カウンセリング・アフターフォローも徹底重視</p>
      </div>
    </div>
  </div>
</body>
</html>
```